Letterhead for clinic notes, test reports, and business cards

I need business card and letterheads for a medical clinic with the following:
1- Business cards. The back should allow for space for date and time of next appointments (few lines would do)
2- Letterhead for clinic notes
3- Letterhead for test reports.

Feel free to use whats included for examples. I value creativity so be creative.

Target Market(s)

Patients, referring physicians.

Industry/Entity Type

Health Care

Requirements
Must have
• Must use current logo.
• Must look good on white background
• Letterhead and reports must look good faxed.
• Please use themes of the current logo. Another possible color to use is grey as well (www.brambleveincare.org - use the font color in the text of that website)

```html
<!DOCTYPE html>
<html lang="en">
<head>
<meta charset="utf-8">
<title>Bramblevein Heart Institute – Letterhead</title>
<link rel="stylesheet" href="https://fonts.googleapis.com/css2?family=Arimo:wght@400;700&family=Source+Sans+3:wght@400&display=swap">
<style>
  :root {
    --brand-red: #d0404a;
    --brand-navy: #1b4a80;
    --ink: #111111;
    --band-tint: #f6dadc;
    --paper: #ffffff;
  }
  * { margin: 0; padding: 0; box-sizing: border-box; }
  html, body { width: 927px; height: 1200px; overflow: hidden; background: var(--paper); }
  .letterhead {
    position: relative;
    width: 927px;
    height: 1200px;
    background: var(--paper);
    font-family: "Arimo", Arial, sans-serif;
    color: var(--ink);
  }
  .side-bar {
    position: absolute; left: 0; top: 0;
    width: 34px; height: 1200px;
    background: var(--brand-red);
  }
  .brand-dot {
    position: absolute; left: 68px; top: 30px;
    width: 170px; height: 170px; border-radius: 50%;
    background: var(--brand-red);
  }
  .brand-name {
    position: absolute; left: 300px; top: 56px; width: 590px;
    font-family: "Arimo", Arial, sans-serif;
    font-weight: 700;
    color: var(--brand-navy);
    text-align: center;
    line-height: 1;
  }
  .brand-name .line-main { display: block; font-size: 49px; letter-spacing: 1px; }
  .brand-name .line-sub { display: block; font-size: 42px; letter-spacing: 1px; margin-top: 14px; }
  .header-rule {
    position: absolute; left: 34px; right: 0; top: 225px;
    height: 1.5px; background: var(--brand-red);
  }
  .letter-body { position: absolute; left: 93px; top: 0; width: 720px; }
  .date { position: absolute; top: 308px; font-size: 12.5px; white-space: nowrap; }
  .recipient { position: absolute; top: 356px; font-size: 12.5px; line-height: 16.3px; }
  .salutation { position: absolute; top: 451px; font-size: 15.5px; font-weight: 700; }
  .paragraph { position: absolute; font-size: 16px; line-height: 20px; white-space: nowrap; }
  .paragraph span { display: block; }
  .para-one { top: 498px; }
  .para-two { top: 669px; }
  .close { position: absolute; top: 821px; font-size: 16px; }
  .sender { position: absolute; top: 894px; font-size: 13px; }
  .sender strong { font-weight: 700; }
  .sender-title { position: absolute; top: 919px; font-size: 16px; }
  .copies { position: absolute; top: 962px; font-size: 16px; }
  .pulse-band {
    position: absolute; left: 34px; right: 0; top: 1040px; height: 84px;
    background: linear-gradient(180deg, var(--paper) 0%, var(--band-tint) 50%, var(--paper) 100%);
  }
  .footer-contact {
    position: absolute; top: 1133px;
    font-family: "Source Sans 3", "Myriad Pro", sans-serif;
    color: var(--brand-red);
    font-size: 18.5px; line-height: 24px; white-space: nowrap;
  }
  .footer-address { left: 54px; }
  .footer-phone { left: 535px; }
  .footer-fax { left: 753px; }
</style>
</head>
<body>
<div class="letterhead">
  <div class="side-bar"></div>

  <header class="brand">
    <div class="brand-dot"></div>
    <div class="brand-name"><span class="line-main">BRAMBLEVEIN HEART</span><span class="line-sub">INSTITUTE</span></div>
  </header>
  <div class="header-rule"></div>

  <main class="letter-body">
    <p class="date">Date : 11/27/16</p>
    <p class="recipient">Sample Address,<br>Sample Street,<br>Near ABC,<br>City name</p>
    <p class="salutation">Salutation :</p>
    <p class="paragraph para-one">
      <span>Lorem Ipsum is simply dummy text of the printing and typesetting industry. Lorem Ipsum has</span>
      <span>been the industry's standard dummy text ever since the 1500s, when an unknown printer took a</span>
      <span>galley of type and scrambled it to make a type specimen book. It has survived not only five</span>
      <span>centuries, but also the leap into electronic typesetting, remaining essentially unchanged. It was</span>
      <span>popularised in the 1960s with the release of Tessaform sheets containing Lorem Ipsum passages,</span>
      <span>and more recently with desktop publishing software like Quillon PageSmith including versions</span>
      <span>&nbsp;of Lorem Ipsum.</span>
    </p>
    <p class="paragraph para-two">
      <span>Lorem Ipsum is simply dummy text of the printing and typesetting industry. Lorem Ipsum has</span>
      <span>been the industry's standard dummy text ever since the 1500s, when an unknown printer took a</span>
      <span>galley of type and scrambled it to make a type specimen book. It has survived not only five</span>
      <span>centuries, but also the leap into electronic typesetting, remaining essentially unchanged.</span>
    </p>
    <p class="close">Complimentary close,</p>
    <p class="sender"><strong>Name of Sender :</strong> Dr. XYZ</p>
    <p class="sender-title">Title</p>
    <p class="copies">CC/cc</p>
  </main>

  <div class="pulse-band" role="img" aria-label="Repeating red heartbeat trace running across the page"></div>

  <footer>
    <p class="footer-contact footer-address">1180 Larkfield Road, Suite 304<br>Ashbury ON K2P4L7</p>
    <p class="footer-contact footer-phone">phone&nbsp; :&nbsp; 555-014-2270<br>email&nbsp; :&nbsp; contact@brambleveincare.org</p>
    <p class="footer-contact footer-fax">fax :&nbsp; 555-014-2281</p>
  </footer>
</div>
</body>
</html>
```